TROMP Diagnostics App - iOS

I need some UI artwork (2D) for my already released iOS app: "TROMP Kv" I'd like the UI to look more like an in-dash head-unit in a car. I'm in the process of updating the app with iPad support and would like to release this next version with a brand new UI.

A lot of car audio enthusiast already use my app and probably mount their iPhone/iPod near their car audio components on the dash. Most of the car audio deck Mfgs support a few colors: Green/Blue/Amber/Red I'd like to offer these themes as well. But I will settle for the Amber color to match my existing App icon scheme. (nice to have)

My UI is incredibly simple. It's just a bunch of up/down buttons. I plan to do some animations an will need some room blocked off for this to the left of LCD text.

Screenshots are of my existing iOS app for iPhone and the half assed job I did for iPad. - Note: These are the only two orientations I plan to use. But the resolution in these photos are smaller than my requirements. See "Must Haves" for all four resolutions.

update: I'd like something to imitate the style of the skin in the following: http://quorvak.pelmintra.example/art/Lumatone-XJR8-Skin-71845206

Thanks!

Target Market(s)

Car Audio Enthusiasts

Industry/Entity Type

Audio

Requirements
Must have
• - Static background that looks like an in-dash stereo. (think lumatone skin)
- An LCD area where I can display some text and stats on left (see iPad ss)
- UI buttons that support up/down states. When the user presses a button, it stays "down" until it's tapped again or another is pushed.
- UI toggle switch for Wobble mode (see ss)

iPhone/iPod resolutions
-
- Landscape for iPhone4/4S Retina (960 x 640)
- Landscape for iPhone 5 Retina (1136 x 640)

iPad resolutions
-
- This UI has more buttons and taller, but I'd like a similar look and feel
- Landscape for iPad Retina (2048 x 1536)
- Landscape for iPad2/mini (1024 x 768)

Other Controls:
- An empty space for UI slider control. I will place this over artwork. (see ss)
- Emergency stop button should be red and easily accessible. Slightly larger than other buttons.

iPhone Buttons/Controls
-
20,30,40,50,60,70,80,90,100,150,250,300
Toggle Switch, P button, S button, Stop button

iPad Buttons/Controls
-
20,25,30,35,40,45,50,55,60,65,70,80,90,110,125,150,250,300
Instant TROMP Buttons: 20,25,30,35,40,45,50,55

Disregard the waveform animation in the screenshots (squiggly line at bottom) I plan do a small animation to the left of the text in the LCD area.
Nice to have
• - Theme for LED-like colors: Green/Blue/Amber/Red on-off buttons
Should not have
• - sharp corners on buttons
- stretched version of iPhone layout for the iPad.

```html
<!DOCTYPE html>
<html lang="en">
<head>
<meta charset="utf-8">
<title>TROMP Kv – Frequency Tones</title>
<link href="https://fonts.googleapis.com/css2?family=Orbitron:wght@500;700;900&display=swap" rel="stylesheet">
<style>
  :root {
    --canvas: #0b0c0d;
    --mesh-light: #2a2c2f;
    --mesh-dark: #0f1011;
    --speaker-center: #4a4d50;
    --speaker-mid: #141516;
    --speaker-rim: #7a7e82;
    --label: #e6ecef;
    --lcd-top: #5cc8f2;
    --lcd-bottom: #1b88c9;
    --lcd-text: #f2fbff;
    --bezel-light: #d9dcdf;
    --bezel-dark: #6d7276;
    --btn-light: #7fd3f5;
    --btn-mid: #1f8fc7;
    --btn-dark: #0d4f78;
    --btn-ring: #0a2a40;
    --btn-glow: rgba(90, 200, 255, 0.55);
    --btn-text: #ffffff;
    --square-top: #2e8fbf;
    --square-bottom: #0f4a6c;
    --square-edge: #5fb9e3;
    --track: #9a9da0;
    --knob: #e0201c;
    --stop-top: #ff3a33;
    --stop-bottom: #8a0000;
    --stop-glow: rgba(255, 40, 30, 0.6);
    --toggle-body: #8e9397;
  }
  * { box-sizing: border-box; margin: 0; padding: 0; }
  html, body { width: 1200px; height: 938px; overflow: hidden; background: var(--canvas); }
  body { font-family: "Orbitron", sans-serif; }

  .head-unit { position: relative; width: 1200px; height: 938px; }

  .mesh-backdrop {
    position: absolute; inset: 0;
    background: radial-gradient(ellipse at 50% 45%, var(--mesh-light), var(--mesh-dark) 80%);
  }

  .speaker {
    position: absolute;
    width: 184px; height: 184px;
    border-radius: 50%;
    background: radial-gradient(circle, var(--speaker-center), var(--speaker-mid) 62%, var(--speaker-rim) 100%);
  }
  .speaker--left { left: 32px; top: 47px; }
  .speaker--right { left: 1003px; top: 47px; }

  .lcd {
    position: absolute;
    left: 249px; top: 20px;
    width: 706px; height: 224px;
    border-radius: 0 0 34px 34px;
    background: linear-gradient(180deg, var(--bezel-light), var(--bezel-dark));
    padding: 14px;
  }
  .lcd__screen {
    width: 100%; height: 100%;
    border-radius: 0 0 26px 26px;
    background: linear-gradient(180deg, var(--lcd-top), var(--lcd-bottom));
    box-shadow: inset 0 0 18px rgba(0,40,80,0.6);
    display: flex; align-items: center; justify-content: center;
    color: var(--lcd-text);
    font-weight: 900;
    font-size: 112px;
    letter-spacing: 4px;
  }
  .lcd__unit { font-size: 96px; margin-left: 34px; }

  .section-label {
    position: absolute;
    transform: translateX(-50%);
    color: var(--label);
    font-size: 17px;
    font-weight: 500;
    letter-spacing: 2px;
    white-space: nowrap;
  }

  .tone-btn {
    position: absolute;
    width: 96px; height: 96px;
    margin: -48px 0 0 -48px;
    border-radius: 50%;
    background: radial-gradient(circle at 50% 30%, var(--btn-light), var(--btn-mid) 55%, var(--btn-dark));
    border: 4px solid var(--btn-ring);
    box-shadow: 0 0 14px var(--btn-glow), inset 0 -6px 10px rgba(0,0,0,0.35);
    color: var(--btn-text);
    font-size: 30px; font-weight: 700;
    display: flex; align-items: center; justify-content: center;
  }

  .instant-btn {
    position: absolute;
    width: 96px; height: 58px;
    border-radius: 6px;
    background: linear-gradient(180deg, var(--square-top), var(--square-bottom));
    border: 2px solid var(--square-edge);
    box-shadow: 0 0 8px var(--btn-glow);
    color: var(--btn-text);
    font-size: 26px; font-weight: 700;
    display: flex; align-items: center; justify-content: center;
  }

  .slider-track {
    position: absolute;
    left: 73px; top: 709px;
    width: 749px; height: 6px;
    border-radius: 3px;
    background: var(--track);
  }
  .slider-knob {
    position: absolute;
    left: 266px; top: 699px;
    width: 26px; height: 26px;
    border-radius: 50%;
    background: radial-gradient(circle at 40% 35%, #ff6a60, var(--knob) 60%, #7a0c08);
  }

  .toggle {
    position: absolute;
    left: 76px; top: 808px;
    width: 157px; height: 66px;
    border-radius: 33px;
    background: linear-gradient(180deg, #b9bdc0, #55595c);
    border: 2px solid #2a2c2e;
    display: flex; align-items: center; justify-content: flex-end;
    padding-right: 22px;
    color: #f4f6f7;
    font-size: 18px; font-weight: 700;
  }
  .toggle__knob {
    position: absolute;
    left: 4px; top: 4px;
    width: 56px; height: 56px;
    border-radius: 50%;
    background: radial-gradient(circle at 40% 35%, #f2f3f4, var(--toggle-body) 70%, #3c3f42);
  }

  .mode-btn {
    position: absolute;
    top: 804px;
    width: 107px; height: 67px;
    border-radius: 6px;
    background: linear-gradient(180deg, var(--square-top), var(--square-bottom));
    border: 2px solid var(--square-edge);
    box-shadow: 0 0 8px var(--btn-glow);
    color: var(--btn-text);
    font-size: 30px; font-weight: 700;
    display: flex; align-items: center; justify-content: center;
  }
  .mode-btn--sweep { left: 390px; }
  .mode-btn--noise { left: 667px; }

  .stop-btn {
    position: absolute;
    left: 942px; top: 775px;
    width: 228px; height: 80px;
    border-radius: 22px;
    background: linear-gradient(180deg, var(--stop-top), var(--stop-bottom));
    border: 3px solid #3a0000;
    box-shadow: 0 0 22px var(--stop-glow);
    color: #ffe5e3;
    font-size: 30px; font-weight: 700;
    letter-spacing: 3px;
    display: flex; align-items: center; justify-content: center;
  }
</style>
</head>
<body>
<main class="head-unit">
  <div class="mesh-backdrop" role="img" aria-label="Dark hexagonal metal mesh texture"></div>

  <div class="speaker speaker--left" role="img" aria-label="Speaker grille"></div>
  <div class="speaker speaker--right" role="img" aria-label="Speaker grille"></div>

  <div class="lcd">
    <div class="lcd__screen">0.0<span class="lcd__unit">Hz</span></div>
  </div>

  <div class="section-label" style="left:445px; top:268px;">FREQUENCY TONES</div>

  <div class="tone-btn" style="left:124px; top:353px;">20</div>
  <div class="tone-btn" style="left:250px; top:353px;">20</div>
  <div class="tone-btn" style="left:377px; top:353px;">20</div>
  <div class="tone-btn" style="left:503px; top:353px;">20</div>
  <div class="tone-btn" style="left:630px; top:353px;">20</div>
  <div class="tone-btn" style="left:756px; top:353px;">20</div>

  <div class="tone-btn" style="left:124px; top:464px;">50</div>
  <div class="tone-btn" style="left:250px; top:464px;">50</div>
  <div class="tone-btn" style="left:377px; top:464px;">50</div>
  <div class="tone-btn" style="left:503px; top:464px;">50</div>
  <div class="tone-btn" style="left:630px; top:464px;">50</div>
  <div class="tone-btn" style="left:756px; top:464px;">50</div>

  <div class="tone-btn" style="left:124px; top:576px;">90</div>
  <div class="tone-btn" style="left:250px; top:576px;">90</div>
  <div class="tone-btn" style="left:377px; top:576px;">90</div>
  <div class="tone-btn" style="left:503px; top:576px;">90</div>
  <div class="tone-btn" style="left:630px; top:576px;">90</div>
  <div class="tone-btn" style="left:756px; top:576px;">90</div>

  <div class="section-label" style="left:1038px; top:287px;">INSTAT TROMP</div>

  <div class="instant-btn" style="left:933px; top:324px;">20</div>
  <div class="instant-btn" style="left:1048px; top:324px;">20</div>
  <div class="instant-btn" style="left:933px; top:408px;">50</div>
  <div class="instant-btn" style="left:1048px; top:408px;">50</div>
  <div class="instant-btn" style="left:933px; top:492px;">20</div>
  <div class="instant-btn" style="left:1048px; top:492px;">20</div>
  <div class="instant-btn" style="left:933px; top:574px;">50</div>
  <div class="instant-btn" style="left:1048px; top:574px;">50</div>

  <div class="section-label" style="left:422px; top:662px;">FREQUENCY MODIFIER</div>
  <div class="slider-track"></div>
  <div class="slider-knob"></div>

  <div class="section-label" style="left:166px; top:763px;">+10 HZ WOBBLE</div>
  <div class="section-label" style="left:444px; top:763px;">FREQ. SWEEP</div>
  <div class="section-label" style="left:720px; top:763px;">PINK NOISE</div>

  <div class="toggle"><span class="toggle__knob"></span>OFF</div>
  <div class="mode-btn mode-btn--sweep">S</div>
  <div class="mode-btn mode-btn--noise">P</div>

  <div class="stop-btn">STOP</div>
</main>
</body>
</html>
```